B.O.G
Brenwick Orchard Group
I need double sided standard sized Business Card [3.5" x 2"]
Any fonts
Professional
Linh Tran
President
3318 Velmont Ave
Calder Falls, OR 97352
1-800-555-0147
info@velmorik.com
www.velmorik.com
Anything

```html
<!DOCTYPE html>
<html lang="en">
<head>
<meta charset="utf-8">
<title>Brenwick Orchard Group Stationery</title>
<link href="https://fonts.googleapis.com/css2?family=Open+Sans:wght@400;600;700;800&display=swap" rel="stylesheet">
<style>
  :root {
    --bg: #e9e6e1;
    --paper: #ffffff;
    --blue: #1f3f9c;
    --blue-deep: #132c78;
    --blue-light: #3b63c9;
    --green: #3aa335;
    --ink: #3c3c3c;
    --muted: #777777;
    --on-blue: #e6ecff;
  }
  * { margin: 0; padding: 0; box-sizing: border-box; }
  html, body { width: 1200px; height: 751px; overflow: hidden; }
  body { background: var(--bg); font-family: "Open Sans", Arial, sans-serif; color: var(--ink); position: relative; }
  .sheet { position: absolute; background: var(--paper); box-shadow: 0 2px 6px rgba(0,0,0,.18); overflow: hidden; }
  .wave { position: absolute; left: 0; bottom: 0; width: 100%; }
  .brand { position: absolute; display: flex; align-items: center; gap: 6px; }
  .brand-dot { border-radius: 50%; background: var(--blue); flex: none; }
  .brand-name { font-weight: 800; color: var(--blue); line-height: 1; white-space: nowrap; }

  /* business card front */
  .card-front { left: 67px; top: 29px; width: 221px; height: 126px; }
  .card-front .brand { left: 14px; top: 44px; }
  .card-front .brand-dot { width: 14px; height: 14px; }
  .card-front .brand-name { font-size: 18px; }
  .card-details { position: absolute; left: 112px; top: 12px; font-size: 5px; line-height: 1.55; color: var(--muted); white-space: nowrap; }
  .card-details .person { font-size: 6.5px; font-weight: 700; color: var(--ink); }
  .card-details .role { margin-bottom: 5px; }

  /* business card back */
  .card-back { left: 300px; top: 29px; width: 221px; height: 126px;
    background: radial-gradient(ellipse at 50% 40%, var(--blue-light), var(--blue-deep) 80%); }
  .card-back .site { position: absolute; left: 0; right: 0; top: 70px; text-align: center; font-size: 5.5px; color: var(--on-blue); }

  /* envelope front */
  .envelope-front { left: 19px; top: 180px; width: 600px; height: 216px; }
  .envelope-front .brand { left: 24px; top: 26px; }
  .envelope-front .brand-dot { width: 20px; height: 20px; }
  .envelope-front .brand-name { font-size: 28px; }
  .return-address { position: absolute; left: 24px; top: 146px; font-size: 5px; line-height: 1.55; color: var(--muted); white-space: nowrap; }
  .envelope-front .site { position: absolute; right: 18px; bottom: 8px; font-size: 5.5px; color: var(--on-blue); }

  /* envelope back */
  .envelope-back { left: 19px; top: 468px; width: 600px; height: 252px; }
  .envelope-back svg { position: absolute; left: 0; top: 0; width: 100%; height: 100%; }
  .envelope-back .brand { left: 0; right: 0; top: 22px; justify-content: center; }
  .envelope-back .brand-dot { width: 14px; height: 14px; background: var(--on-blue); }
  .envelope-back .brand-name { font-size: 20px; color: var(--on-blue); }

  /* letterhead */
  .letterhead { left: 628px; top: 19px; width: 552px; height: 715px; }
  .letterhead .brand { left: 24px; top: 40px; }
  .letterhead .brand-dot { width: 20px; height: 20px; }
  .letterhead .brand-name { font-size: 28px; }
  .letter { position: absolute; left: 24px; top: 112px; width: 500px; font-size: 5px; line-height: 1.7; color: var(--ink); }
  .letter p { margin-bottom: 9px; }
  .letter .addressee { margin-bottom: 22px; }
  .letter .sign-off { margin-top: 150px; }
  .letterhead .footer-address { position: absolute; left: 24px; bottom: 40px; font-size: 5px; line-height: 1.55; color: var(--muted); white-space: nowrap; }
  .letterhead .site { position: absolute; right: 22px; bottom: 10px; font-size: 5.5px; color: var(--on-blue); }
</style>
</head>
<body>

<section class="sheet card-front" aria-label="Business card front">
  <div class="brand"><span class="brand-dot"></span><span class="brand-name">B.O.G</span></div>
  <div class="card-details">
    <div class="person">Linh Tran</div>
    <div class="role">President</div>
    <div>3318 Velmont Ave</div>
    <div>Calder Falls, OR 97352</div>
    <div>Tel: 1-800-555-0147</div>
    <div>info@velmorik.com</div>
    <div>www.velmorik.com</div>
  </div>
  <svg class="wave" viewBox="0 0 221 36" height="36" preserveAspectRatio="none" aria-hidden="true">
    <path d="M0 32 C70 36 140 26 221 4 L221 36 L0 36Z" fill="var(--green)"/>
    <path d="M0 35 C80 36 150 30 221 12 L221 36 L0 36Z" fill="var(--blue)"/>
  </svg>
</section>

<section class="sheet card-back" aria-label="Business card back">
  <svg class="wave" viewBox="0 0 221 36" height="36" preserveAspectRatio="none" aria-hidden="true">
    <path d="M0 16 C70 30 150 28 221 12 L221 36 L0 36Z" fill="var(--green)"/>
    <path d="M0 20 C70 34 150 32 221 17 L221 36 L0 36Z" fill="var(--blue-deep)"/>
  </svg>
  <div class="site">www.velmorik.com</div>
</section>

<section class="sheet envelope-front" aria-label="Envelope front">
  <div class="brand"><span class="brand-dot"></span><span class="brand-name">B.O.G</span></div>
  <div class="return-address">
    <div>3318 Velmont Ave, Calder Falls, OR 97352</div>
    <div>Tel: 1-800-555-0147 &nbsp;|&nbsp; info@velmorik.com</div>
  </div>
  <svg class="wave" viewBox="0 0 600 56" height="56" preserveAspectRatio="none" aria-hidden="true">
    <path d="M0 54 C200 56 400 44 600 6 L600 56 L0 56Z" fill="var(--green)"/>
    <path d="M180 56 C340 54 480 42 600 16 L600 56Z" fill="var(--blue)"/>
  </svg>
  <div class="site">www.velmorik.com</div>
</section>

<section class="sheet envelope-back" aria-label="Envelope back">
  <svg viewBox="0 0 600 252" preserveAspectRatio="none" aria-hidden="true">
    <path d="M0 252 L250 118 M600 252 L350 118" stroke="#e4e4e4" stroke-width="1" fill="none"/>
    <path d="M0 0 H600 V14 L310 118 Q300 121 290 118 L0 14Z" fill="var(--green)"/>
    <path d="M0 0 H600 V6 L310 109 Q300 112 290 109 L0 6Z" fill="var(--blue)"/>
  </svg>
  <div class="brand"><span class="brand-dot"></span><span class="brand-name">B.O.G</span></div>
</section>

<section class="sheet letterhead" aria-label="Letterhead">
  <div class="brand"><span class="brand-dot"></span><span class="brand-name">B.O.G</span></div>
  <div class="letter">
    <p class="addressee">Name Surname<br>Title<br>Company Name<br>Street Address<br>City, State Zip</p>
    <p>Dear Ms. Harlow,</p>
    <p>Thank you for your interest in our orchard services. We are pleased to share our seasonal program, covering planting, pruning, harvest and distribution for growers across the region. Our team has served local farms for many years with care and reliability, and we take pride in every tree we tend.</p>
    <p>Enclosed you will find a summary of our rates and a sample schedule. Each plan can be adjusted to suit the size of your orchard and the timing of your crop, with regular visits from our field staff throughout the year.</p>
    <p>We would welcome the chance to visit your site and discuss your goals in person. Please contact our office at your convenience to arrange a meeting. We look forward to working with you.</p>
    <p class="sign-off">Sincerely,<br><br><br>Linh Tran</p>
  </div>
  <div class="footer-address">
    <div>3318 Velmont Ave, Calder Falls, OR 97352</div>
    <div>Tel: 1-800-555-0147 &nbsp;|&nbsp; info@velmorik.com</div>
  </div>
  <svg class="wave" viewBox="0 0 552 60" height="60" preserveAspectRatio="none" aria-hidden="true">
    <path d="M0 58 C190 60 380 46 552 6 L552 60 L0 60Z" fill="var(--green)"/>
    <path d="M170 60 C320 58 450 44 552 18 L552 60Z" fill="var(--blue)"/>
  </svg>
  <div class="site">www.velmorik.com</div>
</section>

</body>
</html>
```